Velmora Investments - stationery for luxury, exclusive property investment company

We need stationery (letterhead, folder, compliments slip and envelope) and business cards which will reflect our luxury brand.

I have attached some design examples that we like.

We are an investment company which buys property to provide accommodation for corporate customers.

The design of the stationery needs to be be simple, refined, understated, luxury and very tasteful.

The design should communicate luxury and exclusivity, without being ostentatious.

Logo files are attached
Updates

Please can designers re-read the brief, and make sure the logo is in gold on either on a navy or white background.

Target Market(s)

Wealthy customers

Contact Information for Business Card

Laura Penhaligon-Ward
Director
Velmora Investments Limited
email: laura@velmorainvestments-example.co.uk
mob: 07700900412

Font styles to use
Serif

Colors

Designer to choose colors to be used in the design.

Requirements
Must have
• The logo must be gold on either a white or navy background as per the attached logos.
• The stationery MUST have the following information:
• Velmora Investments Limited
• The Larches
• Wexley Rise
• Marlowden
• ZX19 2QP
• Company Number: 48273615 (Registered in England and Wales)
• The letterhead must also have the two attached logos for the KPV and the KPV accreditation scheme. They do not need to be large.
Nice to have
• A watermark, navy banding either top or bottom.
Should not have
• Anything that looks budget.

```html
<!DOCTYPE html>
<html lang="en">
<head>
<meta charset="utf-8">
<title>Velmora Investments – Stationery Set</title>
<link rel="stylesheet" href="https://fonts.googleapis.com/css2?family=Cinzel:wght@500&family=Jost:wght@300;400&display=swap">
<style>
  :root{
    --gold:#c4a15a;
    --navy:#06062f;
    --navy-card:#17163f;
    --band:#272240;
    --paper:#ffffff;
    --label:#b9b9b9;
    --line:#d4d4d4;
    --badge:#e0353b;
    --inside-a:#eef0f2;
    --inside-b:#e3e6e9;
  }
  *{box-sizing:border-box;margin:0;padding:0}
  html,body{width:1050px;height:1200px;overflow:hidden;background:#fff}
  .sheet{position:relative;width:1050px;height:1200px;border:1px solid #9a9a9a;background:#fff;font-family:'Jost',sans-serif}
  .piece{position:absolute;background:var(--paper)}
  .label{position:absolute;font-family:'Jost',sans-serif;font-weight:300;color:var(--label);font-size:17px;transform:translateX(-50%);white-space:nowrap}

  /* brand lockup */
  .brand{position:absolute;display:flex;flex-direction:column;align-items:center;transform:translateX(-50%);color:var(--gold);font-family:'Cinzel',serif;font-weight:500;text-align:center;line-height:1}
  .brand-dot{border-radius:50%;background:var(--gold);margin-bottom:6px}
  .brand-name{letter-spacing:.04em}
  .brand-sub{letter-spacing:.32em;margin-top:3px}
  .brand-reg{font-family:'Jost',sans-serif;font-weight:300;font-size:4.5px;margin-top:5px;line-height:1.5;letter-spacing:0}

  /* letterhead */
  .letterhead{left:78px;top:55px;width:437px;height:620px;box-shadow:0 4px 18px rgba(0,0,0,.18)}
  .letterhead .address{position:absolute;right:26px;top:68px;text-align:right;color:var(--gold);font-weight:300;font-size:7px;line-height:12px}
  .letterhead .band{position:absolute;left:377px;top:135px;width:39px;height:485px;background:var(--band)}
  .accreditation{position:absolute;top:597px;height:12px;background:var(--badge)}

  /* business card */
  .bcard{left:116px;top:521px;width:196px;height:114px;background:var(--navy-card);box-shadow:0 3px 10px rgba(0,0,0,.3)}
  .bcard .divider{position:absolute;left:132px;top:16px;width:1px;height:80px;background:var(--gold)}
  .bcard .details{position:absolute;left:138px;top:24px;color:var(--gold);font-weight:300;font-size:6.4px;line-height:10.5px}
  .bcard .details .gap{height:6px}

  /* envelope & comp slip */
  .envelope,.compslip{width:440px;height:211px;border:1px solid var(--line)}
  .envelope{left:540px;top:58px}
  .envelope .window{position:absolute;left:42px;top:90px;width:173px;height:80px;border:1px solid #222;border-radius:4px}
  .envelope .band{position:absolute;right:0;top:105px;width:39px;height:106px;background:var(--band)}
  .compslip{left:540px;top:317px}
  .compslip .footer{position:absolute;left:30px;top:179px;color:var(--gold);font-weight:300;font-size:7px;white-space:nowrap}
  .compslip .band{position:absolute;right:15px;top:49px;width:38px;height:162px;background:var(--band);display:flex;align-items:center;justify-content:center}
  .compslip .band span{transform:rotate(-90deg);color:var(--gold);font-weight:300;font-size:16px;white-space:nowrap;letter-spacing:.02em}

  /* folder */
  .cover{left:57px;top:706px;width:318px;height:452px;background:var(--navy)}
  .inside{left:387px;top:706px;width:609px;height:452px;border:1px solid var(--line);overflow:hidden}
  .inside .pattern{position:absolute;left:0;top:0;width:305px;height:452px;background:radial-gradient(ellipse at 30% 25%,#f7fbfd 0%,var(--inside-a) 55%,var(--inside-b) 100%)}
  .inside .right{position:absolute;left:305px;top:0;width:304px;height:452px;background:linear-gradient(180deg,var(--inside-a),var(--inside-b));border-left:1px solid #d8dbde}
  .inside svg{position:absolute;left:0;top:0}
  .inside .pocket-text{position:absolute;left:340px;top:419px;color:var(--gold);font-weight:300;font-size:6.6px;white-space:nowrap}
</style>
</head>
<body>
<div class="sheet">

  <!-- Letterhead -->
  <div class="piece letterhead">
    <div class="brand" style="left:100px;top:42px">
      <span class="brand-dot" style="width:22px;height:22px"></span>
      <span class="brand-name" style="font-size:15px">VELMORA</span>
      <span class="brand-sub" style="font-size:8px">INVESTMENTS</span>
      <span class="brand-reg">Company Number: 48273615<br>(Registered in England and Wales)</span>
    </div>
    <div class="address">
      Velmora Investments Limited<br>The Larches<br>Wexley Rise<br>Marlowden<br>ZX19 2QP
    </div>
    <div class="band"></div>
    <span class="accreditation" style="left:316px;width:24px" aria-label="Accreditation badge"></span>
    <span class="accreditation" style="left:346px;width:24px" aria-label="Accreditation scheme badge"></span>
  </div>
  <div class="label" style="left:167px;top:224px">Letterhead</div>

  <!-- Business card -->
  <div class="piece bcard">
    <div class="brand" style="left:68px;top:24px">
      <span class="brand-dot" style="width:20px;height:20px"></span>
      <span class="brand-name" style="font-size:13px">VELMORA</span>
      <span class="brand-sub" style="font-size:7px">INVESTMENTS</span>
    </div>
    <div class="divider"></div>
    <div class="details">
      Mara Ellison<br>01632-960418
      <div class="gap"></div>
      The Larches<br>Wexley Rise<br>Marlowden<br>ZX19 2QP
    </div>
  </div>
  <div class="label" style="left:214px;top:642px">b-card</div>

  <!-- Envelope -->
  <div class="piece envelope">
    <div class="brand" style="left:92px;top:28px">
      <span class="brand-dot" style="width:18px;height:18px"></span>
      <span class="brand-name" style="font-size:11px">VELMORA</span>
      <span class="brand-sub" style="font-size:6px">INVESTMENTS</span>
    </div>
    <div class="window"></div>
    <div class="band"></div>
  </div>
  <div class="label" style="left:764px;top:273px">Envelope</div>

  <!-- Compliments slip -->
  <div class="piece compslip">
    <div class="brand" style="left:86px;top:14px">
      <span class="brand-dot" style="width:24px;height:24px"></span>
      <span class="brand-name" style="font-size:15px">VELMORA</span>
      <span class="brand-sub" style="font-size:8px">INVESTMENTS</span>
    </div>
    <div class="footer">Velmora Investments Limited · The Larches · Wexley Rise · Marlowden · ZX19 2QP</div>
    <div class="band"><span>With Compliments</span></div>
  </div>
  <div class="label" style="left:768px;top:541px">Comp Slip</div>

  <!-- Folder cover -->
  <div class="piece cover">
    <div class="brand" style="left:159px;top:184px">
      <span class="brand-dot" style="width:32px;height:32px"></span>
      <span class="brand-name" style="font-size:20px">VELMORA</span>
      <span class="brand-sub" style="font-size:10px">INVESTMENTS</span>
      <span class="brand-reg" style="font-size:5px">Company Number: 48273615<br>(Registered in England and Wales)</span>
    </div>
  </div>
  <div class="label" style="left:216px;top:1162px">Cover</div>

  <!-- Folder inside -->
  <div class="piece inside">
    <div class="pattern" role="img" aria-label="Soft glowing geometric background texture"></div>
    <div class="right"></div>
    <svg width="609" height="452" viewBox="0 0 609 452" aria-hidden="true">
      <defs>
        <linearGradient id="pocketShade" x1="0" y1="0" x2="0" y2="1">
          <stop offset="0" stop-color="#000" stop-opacity="0"/>
          <stop offset="1" stop-color="#000" stop-opacity=".12"/>
        </linearGradient>
      </defs>
      <rect x="399" y="278" width="210" height="18" fill="url(#pocketShade)"/>
      <polygon points="399,296 609,296 609,452 305,452" fill="var(--navy)"/>
    </svg>
    <div class="pocket-text">Velmora Investments Limited · The Larches · Wexley Rise · Marlowden · ZX19 2QP</div>
  </div>
  <div class="label" style="left:698px;top:1164px">Inside</div>

</div>
</body>
</html>
```